Email signature banner for companys 60th anniversary

We are a transportation company. This is what our website people came up with so far:

https://www.plavemockups.com/design/8xWq2LpZr4TnBv7KcYdMfA/Bornel?node-id=4417-35

I want a picture of our transport truck with the decal on the back that we are putting on it.

Our website is www.bornel.com

Target Market(s)

Customer recognition

Industry/Entity Type

fuel and oil distribution company

Requirements
Must have
• our 60th anniversary logo
Nice to have
• Delivering Energy to Build Communites.
Should not have
• picture of the guy from the current banner provided

```html
<!DOCTYPE html>
<html lang="en">
<head>
<meta charset="UTF-8">
<title>Bornel 60th Anniversary Email Banners</title>
<link href="https://fonts.googleapis.com/css2?family=Oswald:wght@500;600&family=Krona+One&family=Playfair+Display:wght@500&family=Poppins:wght@600;700&family=Montserrat:wght@600;700&display=swap" rel="stylesheet">
<style>
  :root {
    --board: #474747;
    --brand-blue: #2b5aab;
    --brand-blue-light: #8fb0e8;
    --brand-red: #d42a2a;
    --ink-dark: #2e2e2e;
    --white: #ffffff;
    --sky: #5a8fd8;
    --sand: #c9b28e;
  }
  * { margin: 0; padding: 0; box-sizing: border-box; }
  html, body { width: 1200px; height: 551px; overflow: hidden; background: var(--board); }
  .board { position: relative; width: 1200px; height: 551px; }

  .banner {
    position: absolute; width: 600px; height: 200px; overflow: hidden;
    background: var(--white); transform: scale(0.88); transform-origin: 0 0;
  }
  .banner--classic { left: 50px; top: 84px; }
  .banner--tagline { left: 620px; top: 84px; }
  .banner--band { left: 50px; top: 299px; }
  .banner--panel { left: 620px; top: 299px; }

  .truck-photo {
    position: absolute; inset: 0;
    background: linear-gradient(180deg, var(--sky) 0%, #9fbde6 38%, #d8d2c4 55%, var(--sand) 72%, #a8916c 100%);
  }
  .white-wedge { position: absolute; inset: 0; background: var(--white); }
  .banner--classic .white-wedge { clip-path: polygon(55.5% 0, 100% 0, 100% 100%, 41% 100%); }
  .banner--tagline .white-wedge { clip-path: polygon(48% 0, 100% 0, 100% 100%, 43% 100%); }

  .centered { position: absolute; text-align: center; white-space: nowrap; transform: translateX(-50%); }

  .brand-name {
    position: absolute; display: flex; align-items: center; gap: 6px;
    font-family: "Oswald", sans-serif; font-weight: 600; color: var(--brand-blue);
    font-size: 26px; line-height: 1;
  }
  .brand-name__dot { width: 14px; height: 14px; border-radius: 50%; background: var(--brand-red); }

  .est { font-family: "Montserrat", sans-serif; font-weight: 600; color: var(--brand-red); font-size: 12px; letter-spacing: 0.5px; }
  .site { font-family: "Montserrat", sans-serif; font-weight: 700; color: var(--brand-blue); font-size: 13px; letter-spacing: 2px; }

  /* Banner 1 */
  .banner--classic .brand-name { left: 420px; top: 22px; font-size: 30px; }
  .banner--classic .headline { left: 472px; top: 90px; font-family: "Oswald", sans-serif; font-weight: 600; font-size: 27px; color: var(--brand-blue); }
  .banner--classic .est { left: 472px; top: 136px; }
  .banner--classic .site { left: 472px; top: 170px; }

  /* Banner 2 */
  .tagline-box {
    position: absolute; left: 0; top: 105px; width: 258px; height: 95px;
    background: rgba(30, 30, 30, 0.55); clip-path: polygon(0 0, 100% 0, 88% 100%, 0 100%);
  }
  .tagline {
    position: absolute; left: 15px; top: 112px; font-family: "Oswald", sans-serif; font-weight: 500;
    color: var(--white); font-size: 27px; line-height: 32px;
  }
  .big-sixty {
    position: absolute; left: 392px; top: -18px; font-family: "Playfair Display", serif; font-weight: 500;
    font-size: 118px; color: var(--brand-blue-light); opacity: 0.75; line-height: 1;
  }
  .banner--tagline .brand-name { left: 476px; top: 30px; font-size: 24px; }
  .extended { font-family: "Krona One", sans-serif; color: var(--brand-blue); font-size: 19px; line-height: 1; font-weight: 400; }
  .banner--tagline .extended--one { left: 478px; top: 105px; }
  .banner--tagline .extended--two { left: 478px; top: 131px; }
  .banner--tagline .est { left: 478px; top: 157px; }
  .banner--tagline .site { left: 478px; top: 177px; }

  /* Banner 3 */
  .frost-band { position: absolute; left: 270px; top: 116px; width: 330px; height: 84px; background: rgba(255,255,255,0.78); }
  .sixty-badge {
    position: absolute; left: 272px; top: 122px; width: 78px; height: 78px; border-radius: 50%;
    background: var(--ink-dark); color: var(--white); display: flex; align-items: center; justify-content: center;
    font-family: "Poppins", sans-serif; font-weight: 700; font-size: 36px;
  }
  .band-celebrating { position: absolute; left: 355px; top: 128px; font-family: "Poppins", sans-serif; font-weight: 600; color: var(--brand-blue); font-size: 17px; line-height: 1; }
  .band-years { position: absolute; left: 353px; top: 146px; font-family: "Poppins", sans-serif; font-weight: 700; color: var(--brand-blue); font-size: 36px; line-height: 1; }
  .banner--band .est { left: 405px; top: 183px; }
  .banner--band .brand-name { left: 480px; top: 133px; font-size: 28px; }
  .banner--band .site { position: absolute; left: 25px; top: 170px; color: var(--white); letter-spacing: 3px; }

  /* Banner 4 */
  .blue-panel { position: absolute; left: 440px; top: 0; width: 160px; height: 200px; background: var(--brand-blue); }
  .panel-copy { position: absolute; left: 520px; top: 40px; text-align: center; transform: translateX(-50%); font-family: "Oswald", sans-serif; font-weight: 500; color: var(--white); white-space: nowrap; }
  .panel-copy__lead { display: block; font-size: 30px; line-height: 36px; }
  .panel-copy__rest { display: block; font-size: 21px; line-height: 27px; }
  .red-strip { position: absolute; left: 440px; top: 150px; width: 160px; height: 33px; background: var(--brand-red); }
  .banner--panel .site { position: absolute; left: 520px; top: 158px; color: var(--white); transform: translateX(-50%); }
  .halo { position: absolute; left: 278px; top: 25px; width: 140px; height: 140px; border-radius: 50%; background: rgba(255,255,255,0.35); }
  .seal {
    position: absolute; left: 288px; top: 35px; width: 120px; height: 120px; border-radius: 50%;
    background: rgba(255,255,255,0.88); text-align: center; color: var(--brand-blue);
  }
  .seal__top { display: block; margin-top: 20px; font-family: "Poppins", sans-serif; font-weight: 600; font-size: 12px; line-height: 1; }
  .seal__num { display: block; font-family: "Playfair Display", serif; font-weight: 500; font-size: 50px; line-height: 46px; }
  .seal__years { display: block; font-family: "Poppins", sans-serif; font-weight: 600; font-size: 16px; line-height: 18px; }
  .seal__est { display: block; font-family: "Montserrat", sans-serif; font-weight: 600; font-size: 8px; color: var(--brand-red); }
  .logo-tab { position: absolute; left: 0; top: 138px; width: 168px; height: 62px; background: rgba(255,255,255,0.85); clip-path: polygon(0 0, 100% 0, 92% 100%, 0 100%); }
  .banner--panel .brand-name { left: 28px; top: 153px; font-size: 28px; }
</style>
</head>
<body>
<main class="board">

  <section class="banner banner--classic">
    <div class="truck-photo" role="img" aria-label="Photo of a white fuel tanker truck parked on sand under a blue sky"></div>
    <div class="white-wedge"></div>
    <div class="brand-name"><span class="brand-name__dot"></span>Bornel</div>
    <p class="centered headline">Celebrating 60 years</p>
    <p class="centered est">EST. 1965</p>
    <p class="centered site">www.bornel.com</p>
  </section>

  <section class="banner banner--tagline">
    <div class="truck-photo" role="img" aria-label="Photo of a white fuel tanker truck parked on sand under a blue sky"></div>
    <div class="white-wedge"></div>
    <div class="tagline-box"></div>
    <p class="tagline">Delivering Energy to<br>Build Communities</p>
    <p class="big-sixty">60</p>
    <div class="brand-name"><span class="brand-name__dot"></span>Bornel</div>
    <p class="centered extended extended--one">CELEBRATING</p>
    <p class="centered extended extended--two">60 YEARS</p>
    <p class="centered est">EST. 1965</p>
    <p class="centered site">www.bornel.com</p>
  </section>

  <section class="banner banner--band">
    <div class="truck-photo" role="img" aria-label="Photo of a white fuel tanker truck on a sandy work site"></div>
    <div class="frost-band"></div>
    <div class="sixty-badge">60</div>
    <p class="band-celebrating">Celebrating</p>
    <p class="band-years">years</p>
    <p class="centered est">EST. 1965</p>
    <div class="brand-name"><span class="brand-name__dot"></span>Bornel</div>
    <p class="site">www.bornel.com</p>
  </section>

  <section class="banner banner--panel">
    <div class="truck-photo" role="img" aria-label="Photo of a white fuel tanker truck on a sandy work site"></div>
    <div class="blue-panel"></div>
    <p class="panel-copy">
      <span class="panel-copy__lead">Delivering</span>
      <span class="panel-copy__rest">Energy to Build</span>
      <span class="panel-copy__rest">Communities</span>
    </p>
    <div class="red-strip"></div>
    <p class="site">www.bornel.com</p>
    <div class="halo"></div>
    <div class="seal">
      <span class="seal__top">Celebrating</span>
      <span class="seal__num">60</span>
      <span class="seal__years">years</span>
      <span class="seal__est">EST. 1965</span>
    </div>
    <div class="logo-tab"></div>
    <div class="brand-name"><span class="brand-name__dot"></span>Bornel</div>
  </section>

</main>
</body>
</html>
```